Restyle 2 infographic/process pages to look professional (improve my effort)

Please restyle the attached pages (1.School Workflow Setup and 2.Workflow). I would like to use this kind of color scheme included in the designs. Make the diagrams simple to follow and professional looking. All should be similar in style, in line with 'metro theme' and in line with 'info-graphic' styling.
Clear, uncluttered, concise.
Winning designer must provide editable files as I may need to edit text...etc.
Align style with www.plurvaco.com
I have also included a flyer that we will be using, so it should align to this too (if possible).
Industry/Entity Type
School

```html
<!DOCTYPE html>
<html lang="en">
<head>
<meta charset="utf-8">
<title>School Workflow Set up</title>
<link rel="stylesheet" href="https://fonts.googleapis.com/css2?family=Source+Sans+3:wght@400;600;700&display=swap">
<style>
  :root {
    --pink: #e6175c;
    --ink: #111111;
    --navy: #2f2b5e;
    --paper: #ffffff;
    --mist: #ececec;
  }
  html, body { margin: 0; padding: 0; overflow: hidden; background: var(--paper); }
  .canvas {
    position: relative; width: 1200px; height: 927px; overflow: hidden;
    background: var(--paper); font-family: "Source Sans 3", Arial, sans-serif;
  }
  .title-bar {
    position: absolute; left: 21px; top: 8px; width: 1152px; height: 70px;
    background: var(--pink); border-radius: 14px; color: var(--paper);
    display: flex; align-items: center; justify-content: center;
    font-size: 60px; font-weight: 400; letter-spacing: 0.5px;
  }
  .diagram { position: absolute; left: 0; top: 0; width: 1200px; height: 927px; }
  .diagram text { font-family: "Source Sans 3", Arial, sans-serif; }
  .label { fill: var(--ink); font-size: 27px; }
  .step-no { fill: var(--paper); font-size: 30px; font-weight: 700; }
  .step-name { fill: var(--paper); font-size: 13px; font-weight: 700; }
  .role { fill: var(--paper); font-size: 18px; font-weight: 700; }
  .role-small { fill: var(--paper); font-size: 12px; font-weight: 700; }
  .parent-name { fill: var(--paper); font-size: 31px; font-weight: 700; }
  .doc-say { fill: var(--ink); font-size: 25px; }
  .doc-text { fill: var(--pink); font-size: 16px; }
  .doc-head { fill: var(--ink); font-size: 16px; }
  .footer-tag {
    position: absolute; left: 12px; top: 812px; color: var(--navy);
    font-size: 16px; font-weight: 700; letter-spacing: 0.2px;
  }
  .hotline {
    position: absolute; left: 12px; top: 843px; width: 333px; height: 65px;
    background: var(--navy); color: var(--paper); display: flex; align-items: center;
    gap: 18px; padding-left: 14px; box-sizing: border-box;
    font-size: 36px; font-weight: 700; letter-spacing: 1px;
  }
  .hotline svg { flex: none; }
  .brand-panel {
    position: absolute; left: 355px; top: 815px; width: 338px; height: 93px;
    background: var(--mist); display: flex; align-items: center; justify-content: center; gap: 12px;
  }
  .brand-dot { width: 40px; height: 40px; border-radius: 50%; background: var(--pink); }
  .brand-name { color: var(--pink); font-size: 42px; font-weight: 700; }
</style>
</head>
<body>
<div class="canvas">
  <div class="title-bar">School Workflow Set up</div>

  <svg class="diagram" viewBox="0 0 1200 927" xmlns="http://www.w3.org/2000/svg">
    <defs>
      <marker id="head" viewBox="0 0 10 10" refX="5" refY="5" markerWidth="3" markerHeight="3" orient="auto">
        <path d="M0,0 L10,5 L0,10 Z" fill="#e6175c"/>
      </marker>
    </defs>

    <!-- Step pills -->
    <g class="step">
      <rect x="27" y="100" width="218" height="112" rx="56" fill="#e6175c"/>
      <path d="M138,100 H83 A56,56 0 0 0 83,212 H138 Z" fill="#111"/>
      <text class="step-no" x="88" y="140" text-anchor="middle">1</text>
      <text class="step-name" x="88" y="170" text-anchor="middle">CREATE</text>
      <text class="step-name" x="88" y="186" text-anchor="middle">MASTER</text>
      <circle cx="186" cy="142" r="30" fill="#fff" role="img" aria-label="Principal person icon"/>
      <text class="role" x="186" y="199" text-anchor="middle">Principal</text>
    </g>
    <g class="step">
      <rect x="27" y="285" width="218" height="112" rx="56" fill="#e6175c"/>
      <path d="M138,285 H83 A56,56 0 0 0 83,397 H138 Z" fill="#111"/>
      <text class="step-no" x="88" y="325" text-anchor="middle">2</text>
      <text class="step-name" x="88" y="355" text-anchor="middle">CREATE</text>
      <text class="step-name" x="88" y="371" text-anchor="middle">CLASS COPY</text>
      <circle cx="186" cy="327" r="30" fill="#fff" role="img" aria-label="Teacher person icon"/>
      <text class="role" x="186" y="386" text-anchor="middle">Teacher</text>
    </g>
    <g class="step">
      <rect x="27" y="470" width="218" height="116" rx="58" fill="#e6175c"/>
      <path d="M138,470 H85 A58,58 0 0 0 85,586 H138 Z" fill="#111"/>
      <text class="step-no" x="88" y="510" text-anchor="middle">3</text>
      <text class="step-name" x="88" y="540" text-anchor="middle">SEND</text>
      <text class="step-name" x="88" y="556" text-anchor="middle">RESPOND</text>
      <circle cx="186" cy="508" r="28" fill="#fff" role="img" aria-label="Excursion coordinator person icon"/>
      <text class="role-small" x="186" y="559" text-anchor="middle">Excursion</text>
      <text class="role-small" x="186" y="574" text-anchor="middle">Co ordinator</text>
    </g>
    <g class="step">
      <rect x="27" y="648" width="218" height="114" rx="57" fill="#e6175c"/>
      <path d="M138,648 H84 A57,57 0 0 0 84,762 H138 Z" fill="#111"/>
      <text class="step-no" x="88" y="688" text-anchor="middle">4</text>
      <text class="step-name" x="88" y="718" text-anchor="middle">TRACK &amp;</text>
      <text class="step-name" x="88" y="734" text-anchor="middle">STORE</text>
      <circle cx="186" cy="690" r="30" fill="#fff" role="img" aria-label="Teacher person icon"/>
      <text class="role" x="186" y="750" text-anchor="middle">Teacher</text>
    </g>

    <!-- Arrows -->
    <g stroke="#e6175c" stroke-width="10" fill="none" marker-end="url(#head)">
      <line x1="176" y1="220" x2="176" y2="266"/>
      <line x1="258" y1="345" x2="515" y2="345"/>
      <line x1="645" y1="333" x2="680" y2="333"/>
      <line x1="802" y1="333" x2="860" y2="333"/>
      <line x1="255" y1="528" x2="298" y2="528"/>
      <line x1="428" y1="528" x2="510" y2="528"/>
      <line x1="579" y1="465" x2="579" y2="418"/>
      <line x1="887" y1="702" x2="264" y2="702"/>
      <line x1="887" y1="142" x2="920" y2="142"/>
      <line x1="887" y1="288" x2="920" y2="288"/>
      <line x1="887" y1="433" x2="920" y2="433"/>
      <line x1="887" y1="579" x2="920" y2="579"/>
      <line x1="887" y1="724" x2="920" y2="724"/>
    </g>
    <line x1="887" y1="132" x2="887" y2="800" stroke="#e6175c" stroke-width="10"/>
    <line x1="887" y1="802" x2="887" y2="828" stroke="#e6175c" stroke-width="10" stroke-dasharray="5 4"/>

    <!-- Labels -->
    <text class="label" x="272" y="324">Find Template</text>
    <text class="label" x="540" y="264">Rename</text>
    <text class="label" x="810" y="293">Send</text>
    <text class="label" x="252" y="490">Find</text>
    <text class="label" x="433" y="490">Modify</text>
    <text class="label" x="677" y="507" text-anchor="middle">Save</text>
    <text class="label" x="677" y="533" text-anchor="middle">as</text>
    <text class="label" x="677" y="559" text-anchor="middle">Final</text>
    <text class="label" x="249" y="664">Receive Consent</text>
    <text class="label" x="485" y="664">Open &amp; Respond to Teacher</text>

    <!-- Documents -->
    <g class="doc">
      <rect x="539" y="276" width="100" height="126" rx="10" fill="#fff" stroke="#e6175c" stroke-width="6"/>
      <line x1="539" y1="314" x2="639" y2="314" stroke="#e6175c" stroke-width="5"/>
      <text class="doc-say" x="546" y="305">say....</text>
      <text class="doc-text" x="548" y="360">zoo</text>
      <text class="doc-text" x="548" y="378">Excursion</text>
      <text class="doc-text" x="548" y="396">MASTER</text>
    </g>
    <g class="doc">
      <rect x="698" y="276" width="97" height="126" rx="10" fill="#fff" stroke="#e6175c" stroke-width="6"/>
      <line x1="698" y1="314" x2="795" y2="314" stroke="#e6175c" stroke-width="5"/>
      <text class="doc-text" x="746" y="338" text-anchor="middle">Save</text>
      <text class="doc-text" x="746" y="356" text-anchor="middle">as</text>
      <text class="doc-text" x="746" y="374" text-anchor="middle">Final</text>
    </g>
    <g class="doc">
      <rect x="316" y="470" width="92" height="120" rx="10" fill="#fff" stroke="#e6175c" stroke-width="6"/>
      <line x1="316" y1="500" x2="408" y2="500" stroke="#e6175c" stroke-width="5"/>
      <text class="doc-head" x="362" y="492" text-anchor="middle">Templete</text>
    </g>
    <g class="doc">
      <rect x="528" y="470" width="102" height="120" rx="10" fill="#fff" stroke="#e6175c" stroke-width="6"/>
      <line x1="528" y1="508" x2="630" y2="508" stroke="#e6175c" stroke-width="5"/>
      <text class="doc-say" x="535" y="499">say....</text>
      <text class="doc-text" x="537" y="548">zoo</text>
      <text class="doc-text" x="537" y="566">Excursion</text>
      <text class="doc-text" x="537" y="584">MASTER</text>
    </g>

    <!-- Mobile phone -->
    <g class="mobile">
      <rect x="643" y="602" width="22" height="40" rx="3" fill="#e6175c"/>
      <rect x="647" y="606" width="14" height="11" fill="#fff"/>
      <g fill="#fff">
        <rect x="647" y="621" width="3" height="3"/><rect x="652" y="621" width="3" height="3"/><rect x="657" y="621" width="3" height="3"/>
        <rect x="647" y="627" width="3" height="3"/><rect x="652" y="627" width="3" height="3"/><rect x="657" y="627" width="3" height="3"/>
        <rect x="647" y="633" width="3" height="3"/><rect x="652" y="633" width="3" height="3"/><rect x="657" y="633" width="3" height="3"/>
      </g>
    </g>

    <!-- Consent responses -->
    <g class="responses">
      <g transform="translate(560,680)"><rect width="46" height="50" rx="7" fill="#fff" stroke="#e6175c" stroke-width="5"/><line x1="0" y1="12" x2="46" y2="12" stroke="#e6175c" stroke-width="4"/><circle cx="23" cy="31" r="13" fill="#e6175c"/><path d="M16,31 L21,36 L30,26" stroke="#fff" stroke-width="3.5" fill="none"/></g>
      <g transform="translate(617,680)"><rect width="46" height="50" rx="7" fill="#fff" stroke="#e6175c" stroke-width="5"/><line x1="0" y1="12" x2="46" y2="12" stroke="#e6175c" stroke-width="4"/><circle cx="23" cy="31" r="13" fill="#e6175c"/><path d="M16,31 L21,36 L30,26" stroke="#fff" stroke-width="3.5" fill="none"/></g>
      <g transform="translate(674,680)"><rect width="46" height="50" rx="7" fill="#fff" stroke="#e6175c" stroke-width="5"/><line x1="0" y1="12" x2="46" y2="12" stroke="#e6175c" stroke-width="4"/><circle cx="23" cy="31" r="13" fill="#e6175c"/><path d="M16,31 L21,36 L30,26" stroke="#fff" stroke-width="3.5" fill="none"/></g>
      <g transform="translate(731,680)"><rect width="46" height="50" rx="7" fill="#fff" stroke="#e6175c" stroke-width="5"/><line x1="0" y1="12" x2="46" y2="12" stroke="#e6175c" stroke-width="4"/><circle cx="23" cy="31" r="13" fill="#e6175c"/><path d="M16,31 L21,36 L30,26" stroke="#fff" stroke-width="3.5" fill="none"/></g>
      <g transform="translate(788,680)"><rect width="46" height="50" rx="7" fill="#fff" stroke="#e6175c" stroke-width="5"/><line x1="0" y1="12" x2="46" y2="12" stroke="#e6175c" stroke-width="4"/><circle cx="23" cy="31" r="13" fill="#e6175c"/><path d="M16,31 L21,36 L30,26" stroke="#fff" stroke-width="3.5" fill="none"/></g>
    </g>

    <!-- Parents -->
    <g class="parent">
      <rect x="942" y="106" width="228" height="72" rx="36" fill="#e6175c"/>
      <circle cx="980" cy="142" r="30" fill="#fff" role="img" aria-label="Parent person icon"/>
      <text class="parent-name" x="1090" y="153" text-anchor="middle">Parent</text>
    </g>
    <g class="parent">
      <rect x="942" y="252" width="228" height="72" rx="36" fill="#e6175c"/>
      <circle cx="980" cy="288" r="30" fill="#fff" role="img" aria-label="Parent person icon"/>
      <text class="parent-name" x="1090" y="299" text-anchor="middle">Parent</text>
    </g>
    <g class="parent">
      <rect x="942" y="397" width="228" height="72" rx="36" fill="#e6175c"/>
      <circle cx="980" cy="433" r="30" fill="#fff" role="img" aria-label="Parent person icon"/>
      <text class="parent-name" x="1090" y="444" text-anchor="middle">Parent</text>
    </g>
    <g class="parent">
      <rect x="942" y="543" width="228" height="72" rx="36" fill="#e6175c"/>
      <circle cx="980" cy="579" r="30" fill="#fff" role="img" aria-label="Parent person icon"/>
      <text class="parent-name" x="1090" y="590" text-anchor="middle">Parent</text>
    </g>
    <g class="parent">
      <rect x="942" y="688" width="228" height="72" rx="36" fill="#e6175c"/>
      <circle cx="980" cy="724" r="30" fill="#fff" role="img" aria-label="Parent person icon"/>
      <text class="parent-name" x="1090" y="735" text-anchor="middle">Parent</text>
    </g>
  </svg>

  <div class="footer-tag">NEW CONSENT MANAGEMENT SYSTEM</div>
  <div class="hotline">
    <svg width="40" height="40" viewBox="0 0 40 40" aria-hidden="true">
      <circle cx="20" cy="20" r="18" fill="none" stroke="#fff" stroke-width="3"/>
      <path d="M14,11 L18,11 L19,16 L16.5,18 C18,21 19.5,22.5 22,24 L24,21.5 L29,22.5 L29,26.5 C29,28 27.5,29 26,29 C18,28 12,22 11,14 C11,12.5 12.5,11 14,11 Z" fill="#fff"/>
    </svg>
    <span>1800 555 019</span>
  </div>
  <div class="brand-panel">
    <div class="brand-dot"></div>
    <span class="brand-name">plurvaco</span>
  </div>
</div>
</body>
</html>
```